Logo + Business Card design for a new start-up

For a new start-up company, a global brand expansion agency (marketing, brand consulting solutions) we're looking for a creative designer to help us design both the company logo and business card for project managers.

The name of the company is 'Harrowgate Market Partners' (abbreviated: HMP, website: harrowgatemarketpartners.example)

The logo design should give the company an image of "corporate" (serious), but not too plain/simple. Playing with overlapping fonts, or font colors is an option. Logo with only the abbreviation HMP is also an option.

The business cards need to have a touch of creativity to them, any style/colors can be used, and should underline the nature of business.

```html
<!DOCTYPE html>
<html lang="en">
<head>
<meta charset="utf-8">
<title>Harrowgate Market Partners – Business Card</title>
<link rel="stylesheet" href="https://fonts.googleapis.com/css2?family=Oswald:wght@500&family=Source+Sans+3:wght@400;600&display=swap">
<style>
  :root {
    --stage: #000000;
    --card-light: #f3f3f3;
    --brand-red: #c00000;
    --ink: #111111;
    --rule-grey: #555555;
    --text-grey: #3a3a3a;
    --white: #ffffff;
  }
  * { margin: 0; padding: 0; box-sizing: border-box; }
  html, body {
    width: 1200px;
    height: 900px;
    overflow: hidden;
    background: var(--stage);
  }
  .canvas {
    position: relative;
    width: 1200px;
    height: 900px;
    background: var(--stage);
  }
  .card {
    position: absolute;
    top: 200px;
    width: 310px;
    height: 502px;
  }
  .card--front {
    left: 265px;
    background: var(--card-light);
    border-radius: 62px 0 72px 0;
  }
  .card--back {
    left: 641px;
    width: 309px;
    background: var(--brand-red);
    border-radius: 0 62px 0 72px;
  }

  /* front: brand lockup */
  .brand-mark {
    position: absolute;
    left: 155px;
    top: 48px;
    width: 38px;
    height: 38px;
    margin-left: -19px;
    background: var(--ink);
  }
  .brand-name {
    position: absolute;
    left: 0;
    width: 100%;
    top: 143px;
    text-align: center;
    font-family: "Oswald", sans-serif;
    font-weight: 500;
    color: var(--brand-red);
    text-transform: uppercase;
    line-height: 1.15;
  }
  .brand-name__main {
    display: block;
    font-size: 27px;
    letter-spacing: 0.2px;
  }
  .brand-name__sub {
    display: flex;
    align-items: center;
    justify-content: center;
    gap: 6px;
    font-size: 18px;
    color: var(--ink);
  }
  .brand-name__sub::before,
  .brand-name__sub::after {
    content: "";
    width: 54px;
    height: 1px;
    background: var(--rule-grey);
  }

  /* front: contact block */
  .contact {
    position: absolute;
    left: 27px;
    top: 327px;
    font-family: "Source Sans 3", sans-serif;
    color: var(--text-grey);
    font-size: 14px;
    line-height: 16px;
  }
  .contact__name {
    font-size: 19px;
    font-weight: 600;
    color: var(--brand-red);
    line-height: 20px;
  }
  .contact__role { margin-top: 4px; }
  .contact__address { margin-top: 19px; }
  .contact__lines { margin-top: 11px; list-style: none; }
  .contact__lines li {
    display: flex;
    align-items: center;
    gap: 6px;
    height: 19px;
  }
  .contact__icon { width: 10px; height: 10px; fill: var(--brand-red); }

  /* back */
  .back-name {
    position: absolute;
    left: 0;
    width: 100%;
    top: 376px;
    text-align: center;
    font-family: "Oswald", sans-serif;
    font-weight: 500;
    color: var(--white);
    text-transform: uppercase;
    line-height: 1.15;
  }
  .back-name__main { display: block; font-size: 32px; }
  .back-name__sub {
    display: flex;
    align-items: center;
    justify-content: center;
    gap: 8px;
    font-size: 22px;
  }
  .back-name__sub::before,
  .back-name__sub::after {
    content: "";
    width: 62px;
    height: 2px;
    background: var(--white);
  }
</style>
</head>
<body>
<main class="canvas">
  <section class="card card--front" aria-label="Business card front">
    <div class="brand-mark" aria-hidden="true"></div>
    <div class="brand-name">
      <span class="brand-name__main">Harrowgate Market</span>
      <span class="brand-name__sub">Partners</span>
    </div>

    <div class="contact">
      <p class="contact__name">DANIEL HARTLEY</p>
      <p class="contact__role">Managing Director</p>
      <p class="contact__address">1234, Address Goes Here<br>Country Name, 123456</p>
      <ul class="contact__lines">
        <li>
          <svg class="contact__icon" viewBox="0 0 10 10" aria-hidden="true">
            <path d="M1 3.2 Q5 0.6 9 3.2 L8.2 4.6 L6.6 4 L6.6 3.2 Q5 2.7 3.4 3.2 L3.4 4 L1.8 4.6 Z M2.4 5.2 H7.6 L8.6 9 H1.4 Z"/>
          </svg>
          <span>555-014-2739</span>
        </li>
        <li>
          <svg class="contact__icon" viewBox="0 0 10 10" aria-hidden="true">
            <path d="M0.5 2 H9.5 V8.4 H0.5 Z" />
            <path d="M0.8 2.3 L5 5.6 L9.2 2.3" fill="none" stroke="#f3f3f3" stroke-width="0.9"/>
          </svg>
          <span>info@harrowgatemarketpartners.example</span>
        </li>
      </ul>
    </div>
  </section>

  <section class="card card--back" aria-label="Business card back">
    <div class="back-name">
      <span class="back-name__main">Harrowgate Market</span>
      <span class="back-name__sub">Partners</span>
    </div>
  </section>
</main>
</body>
</html>
```